New telco company needs a product page

We need to design two pages - one index and one inner.

We are a new telco company and we have developed our own phone. We will be selling our services and the phone on this site.

The design should be easy to understand and use, following the latest trends in Web design, be clean. It should communicate professionalism and integrity.

The name of our company is VORO which stands for Value Over Rush Often. The design should follow this principle.

Our company logo is attached. I can send it in other colors/sizes - let me know.

Target Market(s)

Aging population (70+), middle-aged with parents and grandparents.

Industry/Entity Type

It Company

Requirements
Must have
• index page, inner page, flat, clean, Pellucor 5 style / ZEB style (quintel.example), easy navigation, fluid layout, CSS, tableless
Should not have
• should not use old fonts, should not use old-style design, should not have animation, should not look like QDX or Bimzo (too busy)

```html
<!DOCTYPE html>
<html lang="en">
<head>
<meta charset="utf-8">
<title>VORO — About us</title>
<link rel="stylesheet" href="https://fonts.googleapis.com/css2?family=Jost:wght@300;400&family=Open+Sans:wght@400&display=swap">
<style>
  :root {
    --brand-blue: #1485bb;
    --nav-active: #1a8cc0;
    --nav-text: #333333;
    --logo-grey: #9a9a9a;
    --white: #ffffff;
    --order-red: #cf1620;
    --more-dark: #222222;
    --rule-light: #8fd3f0;
    --footer-text: #333333;
    --device-light: #eef0f3;
    --device-mid: #d4d8de;
  }
  * { margin: 0; padding: 0; box-sizing: border-box; }
  html, body { width: 1200px; height: 708px; overflow: hidden; background: var(--white); }
  .page { position: relative; width: 1200px; height: 708px; font-family: "Jost", sans-serif; }

  .site-header { position: absolute; left: 0; top: 0; width: 1200px; height: 98px; background: var(--white); }
  .brand { position: absolute; left: 129px; top: 24px; display: flex; align-items: center; gap: 8px;
    font-family: "Jost", sans-serif; font-weight: 300; font-size: 44px; line-height: 1; color: var(--logo-grey); letter-spacing: 1px; }
  .brand-mark { width: 12px; height: 12px; background: var(--logo-grey); }
  .main-nav { position: absolute; left: 534px; top: 42px; display: flex; gap: 27px; list-style: none; }
  .main-nav a { font-family: "Jost", sans-serif; font-weight: 300; font-size: 15px; color: var(--nav-text); text-decoration: none; letter-spacing: 0.2px; }
  .main-nav a.is-active { color: var(--nav-active); }
  .social-links { position: absolute; left: 1000px; top: 45px; display: flex; gap: 8px; list-style: none; }
  .social-links a { font-family: "Jost", sans-serif; font-weight: 400; font-size: 10px; color: var(--nav-text); text-decoration: none; }

  .hero { position: absolute; left: 0; top: 98px; width: 1200px; height: 557px; background: var(--brand-blue); overflow: hidden; }
  .hero-title { position: absolute; left: 402px; top: 40px; width: 396px; text-align: center;
    font-weight: 300; font-size: 20.5px; color: var(--white); letter-spacing: 0.3px; line-height: 1; }
  .hero-rule { position: absolute; left: 402px; top: 62px; width: 396px; height: 1px; background: var(--rule-light); }

  .product-visual { position: absolute; left: 139px; top: 110px; width: 479px; height: 460px;
    border-radius: 78px 78px 0 0;
    background: linear-gradient(180deg, var(--device-light) 0%, var(--device-mid) 100%); }

  .feature { position: absolute; left: 651px; top: 192px; color: var(--white); }
  .feature-heading { font-family: "Jost", sans-serif; font-weight: 300; font-size: 55px; line-height: 54px; letter-spacing: -0.3px; }
  .feature-list { list-style: none; margin-top: 14px; font-family: "Open Sans", sans-serif; font-size: 17px; }
  .feature-list li { display: flex; align-items: center; gap: 8px; height: 29px; }
  .feature-list svg { width: 11px; height: 11px; flex: none; }

  .order-button { position: absolute; left: 654px; top: 432px; width: 295px; height: 59px; background: var(--order-red);
    color: var(--white); font-family: "Jost", sans-serif; font-weight: 300; font-size: 25px;
    display: flex; align-items: center; justify-content: center; text-decoration: none; }
  .more-link { position: absolute; left: 822px; top: 492px; width: 127px; height: 24px; background: var(--more-dark);
    color: var(--white); font-family: "Jost", sans-serif; font-weight: 300; font-size: 11px;
    display: flex; align-items: center; justify-content: center; text-decoration: none; }
  .pointer-arrow { position: absolute; left: 955px; top: 475px; }

  .site-footer { position: absolute; left: 0; top: 655px; width: 1200px; height: 53px; background: var(--white);
    display: flex; align-items: center; justify-content: center;
    font-family: "Open Sans", sans-serif; font-size: 10.5px; color: var(--footer-text); }
</style>
</head>
<body>
<div class="page">
  <header class="site-header">
    <div class="brand"><span>voro</span><span class="brand-mark"></span></div>
    <ul class="main-nav">
      <li><a href="#">HOME</a></li>
      <li><a href="#" class="is-active">ABOUT US</a></li>
      <li><a href="#">STORE</a></li>
      <li><a href="#">MY VORO</a></li>
      <li><a href="#">CONTACT US</a></li>
    </ul>
    <ul class="social-links">
      <li><a href="#">Linkora</a></li>
      <li><a href="#">Chirpa</a></li>
      <li><a href="#">Facely</a></li>
    </ul>
  </header>

  <section class="hero">
    <h1 class="hero-title">WELCOME TO VORO</h1>
    <div class="hero-rule"></div>

    <div class="product-visual" role="img" aria-label="Product photo of the VORO phone, white and silver, shown from the top half with the app on screen"></div>

    <div class="feature">
      <h2 class="feature-heading">Lorem ipsum<br>feature dummy text</h2>
      <ul class="feature-list">
        <li><svg viewBox="0 0 12 12"><circle cx="6" cy="6" r="6" fill="#fff"/><path d="M3.2 6.2l1.9 1.8 3.7-3.8" fill="none" stroke="#1485bb" stroke-width="1.6"/></svg>Lorem ipsum dolor sit amet, consectetur adipising</li>
        <li><svg viewBox="0 0 12 12"><circle cx="6" cy="6" r="6" fill="#fff"/><path d="M3.2 6.2l1.9 1.8 3.7-3.8" fill="none" stroke="#1485bb" stroke-width="1.6"/></svg>Donec sem eros, tincidunt at congue posuere amt</li>
        <li><svg viewBox="0 0 12 12"><circle cx="6" cy="6" r="6" fill="#fff"/><path d="M3.2 6.2l1.9 1.8 3.7-3.8" fill="none" stroke="#1485bb" stroke-width="1.6"/></svg>Sed eu est non nisl vehicula bibendum</li>
      </ul>
    </div>

    <a href="#" class="order-button">Click here to order</a>
    <a href="#" class="more-link">Click here to more</a>
    <svg class="pointer-arrow" width="50" height="40" viewBox="0 0 50 40">
      <path d="M46 35 C30 36 16 26 6 4" fill="none" stroke="#fff" stroke-width="1.3"/>
      <path d="M6 4 L5 13 M6 4 L13 9" fill="none" stroke="#fff" stroke-width="1.3"/>
    </svg>
  </section>

  <footer class="site-footer">all right reserved © 2013 - terms and conditions</footer>
</div>
</body>
</html>
```